Lens Troupe Nordic Website - Photography and Films

We are looking for a design that expresses the friendly, open nature of our company Lens Troupe Nordic, yet at the same time is professional looking and functional.

Lens Troupe Nordic is a B2B focused operation that hires out multi-lingual camera crews (and equipment) throughout Germany and Europe. We also produce tv features and coporate films. Our unique selling point is that we are native English speakers who can communicate with our international clients (usually British or American) and organise the logistics of shooting in foreign countries.

For content inspiration, see our current website: http://www.lenstroupenordic.example - however we want to move away from the very simple structure of this site and move towards a layout that displays and allows for frequently updated content (e.g. in the form of a blog).

Here is an example of the kind of clean look we like:
http://www.vistaclipvault.example/gallery/home/reelsvcv.do#reel=48203716

Please keep within the following specifications:
- We wish to keep our logo (grey/white, font: Glypha) and our company colour red (#C40A0A) as they are.
- Maximum Width 960px, on a large browser-window the design should be centred
- Easily readable font sizes with good contrast
- Provide your design in PSD file format
- Our logo should be graphically displayed in the top left of the header.
- The design should allow space for a video.
- The page should have a clearly recognisable end in the form of a footer.

The following menu items need to be clearly arranged so the viewer is not overwhelmed or confused:
About
Services - Crews / Corporate Shoots / Webcasts / Production Arm / Legal Videography
Recent Productions
Blog
Testimonials
Get a Quote
Contact
Film Library
Showreel
Events
Film Location Guide - Frankfurt / Cologne / Zurich / Helsinki / Amsterdam / London / Paris / Rome / Brussels / Berlin / Munich
Updates

Reason: Hi - thanks very much for your interest in our design project.  We are extending this auction because we haven't had enough time to really focus on the desigs and provide immediate feedback to designers.  We will try to provide timely feedback and are giving you more time to make any adjustments to your designs etc.
Thanks!
Maren

Target Market(s)

Our target customers are males and females between 25 and 55 years (mostly British and American). More important than their demographic though, is their occupation - they are largely communication and design savvy individuals belonging to one of the following three categories: 1)Broadcasters (usually producers for example from the VCN or Horizon Network seeking trustworthy, affordable crews for their foreign shoots).

2) Video Production Companies (seeking a trustworthy, affordable partner company to provide the crews for their own corporate clients).

3) Corporate Communications Specialists (seeking professional producers and crews to facilitate production of company videos or filming of events).

Industry/Entity Type

Camera

Requirements
Must have
• A fresh clean appearance with good use of white space.
Should not have
• Avoid dark heavy colours and designs.
• Avoid designs that would be impractical and could potentially take a long time to load.

```html
<!DOCTYPE html>
<html lang="en">
<head>
<meta charset="utf-8">
<title>Lens Troupe Nordic</title>
<link href="https://fonts.googleapis.com/css2?family=Arimo:wght@400;700&display=swap" rel="stylesheet">
<style>
:root{
  --red:#c40a0a;
  --red-dark:#9e0707;
  --red-light:#e0152a;
  --grey:#cfcfcf;
  --grey-mid:#b5b5b5;
  --panel:#d6d6d6;
  --ink:#222;
  --white:#fff;
}
*{box-sizing:border-box;margin:0;padding:0}
html,body{width:1200px;height:2400px;overflow:hidden;background:var(--white)}
body{font-family:"Arimo",Arial,sans-serif;color:var(--ink);position:relative}
.abs{position:absolute}
a{color:inherit;text-decoration:none}

/* header */
.hero{left:0;top:0;width:1200px;height:700px;background:radial-gradient(ellipse at 55% 55%,#f4f4f4 0%,#c9c9c9 35%,#6f6f6f 70%,#2a2a2a 100%)}
.logo{left:299px;top:0;width:194px;height:200px;background:var(--red);color:var(--white);font-weight:700;font-size:37px;line-height:40px;padding:50px 14px 0 16px;letter-spacing:-1px}
.menu{left:499px;top:0;width:200px;height:395px;background:rgba(220,220,220,.92);padding:8px 0 0 27px}
.menu-title{display:block;text-align:center;margin-left:-27px;color:var(--red);font-size:17px}
.menu-caret{display:block;margin:2px 0 16px 72px}
.menu li{list-style:none;font-size:15px;font-weight:700;color:#333;line-height:30.5px}
.menu li.active{color:var(--red)}
.submenu{left:701px;top:200px;width:198px;height:168px;background:var(--red);padding:20px 0 0 34px}
.submenu li{list-style:none;color:var(--white);font-size:16px;font-weight:700;line-height:24px}
.submenu li:first-child{text-decoration:underline}
.flag{right:20px;top:8px;width:34px;height:22px;background:linear-gradient(#000 0 33%,#d00 33% 66%,#fc0 66%)}
.event-date{left:27px;top:528px;color:var(--white);font-size:38px}
.event-text{left:27px;top:576px;width:330px;color:var(--white);font-size:16px;line-height:20px}
.event-link{left:27px;top:662px;background:var(--white);color:var(--red);font-size:14px;font-weight:700;padding:2px 8px}
.share{left:973px;top:645px;width:200px;height:55px;background:rgba(230,230,230,.85);display:flex;align-items:center;gap:7px;padding-left:12px}
.share-label{color:var(--red);font-size:14px;font-weight:700}
.share-item{font-size:11px;font-weight:700;color:#444;display:flex;align-items:center;gap:3px}
.share-item i{display:inline-block;width:10px;height:10px;background:#666}

/* red band + tabs */
.band{left:0;top:700px;width:1200px;height:52px;background:linear-gradient(var(--red-light),var(--red-dark))}
.tab-row{left:0;top:752px;width:1200px;height:48px;background:var(--grey-mid)}
.tab{height:48px;width:197px;background:var(--grey);color:var(--white);font-weight:700;font-size:19px;display:flex;align-items:center;justify-content:center}
.tab-testimonials{left:27px;top:752px}
.tab-quote{left:973px;top:752px;width:200px}

.feature{left:0;top:800px;width:1200px;height:290px;background:var(--panel)}
.quote{left:27px;top:840px;width:555px;font-size:22px;font-weight:700;line-height:28px;color:#111}
.quote-author{left:27px;top:1010px;font-size:24px;font-weight:700}
.quote-more{left:27px;top:1052px;font-size:14px;color:var(--red)}
.divider{left:600px;top:820px;width:1px;height:250px;background:#aaa}
.form{left:640px;top:830px;width:255px}
.field-label{display:block;color:var(--white);font-size:13px;margin-bottom:2px}
.field{display:block;width:245px;height:20px;background:var(--white);border:1px solid #999;margin-bottom:8px}
.btn{display:inline-block;background:#444;color:var(--white);font-size:15px;padding:6px 18px;margin:6px 10px 0 0}
.form-note{font-size:12px;color:var(--white);margin-top:8px;line-height:15px;padding-left:6px}
.message-label{left:933px;top:830px;color:var(--white);font-size:13px}
.message{left:933px;top:849px;width:240px;height:216px;background:var(--white);border:1px solid #999}

.tab-clients{left:27px;top:1097px;height:54px;background:var(--grey);color:var(--white)}
.clients{left:0;top:1178px;width:1200px;height:155px;background:var(--grey)}
.client{font-size:32px;font-weight:700;color:#777;text-align:center}
.arrow{top:1175px}

/* content */
.intro-title{left:27px;top:1342px;width:540px;font-size:29px;font-weight:700;line-height:33px}
.intro{left:27px;top:1440px;width:538px;font-size:17.5px;line-height:34px;color:#333}
.intro p{margin-bottom:34px}
.intro ul{margin:-34px 0 34px 24px}
.intro li{list-style:none;position:relative;padding-left:14px}
.intro li::before{content:"*";position:absolute;left:0}
.intro .link{color:var(--red);text-decoration:underline}

.reel-title{left:600px;top:1345px;font-size:22px}
.video{left:600px;top:1380px;width:573px;height:338px;background:var(--red)}
.video-name{left:600px;top:1500px;width:573px;text-align:center;color:var(--white);font-size:42px;font-weight:700}
.play{left:866px;top:1572px}
.controls{left:600px;top:1718px;width:573px;height:16px;background:#ddd;border-top:1px solid #aaa}
.social{left:600px;top:1768px;display:flex;gap:8px;font-size:13px}
.social span{border:1px solid #aaa;padding:3px 7px;background:#f3f3f3}
.more{left:600px;top:1808px;font-size:22px}
.thumb{width:240px;height:170px;background:var(--red);display:flex;align-items:center;justify-content:center;color:var(--white);font-weight:700;font-size:18px}
.thumb-caption{width:240px;font-size:14px;color:var(--red);line-height:18px;margin-top:6px}
.see-all{left:600px;top:2292px;font-size:22px}

.footer{left:0;top:2347px;width:1200px;height:53px;background:var(--red);color:var(--white);padding:8px 27px}
.footer-nav{font-size:14px;font-weight:700}
.footer-legal{font-size:12px;margin-top:5px}
</style>
</head>
<body>

<header>
  <div class="abs hero" role="img" aria-label="Close-up photo of a professional video camera with a film light"></div>
  <a class="abs logo" href="#">lens<br>troupe<br>nordic</a>
  <nav class="abs menu">
    <span class="menu-title">menu</span>
    <svg class="menu-caret" width="16" height="10" viewBox="0 0 16 10"><path d="M1 1 L8 8 L15 1" stroke="#c40a0a" stroke-width="3" fill="none"/></svg>
    <ul>
      <li>[] About Us</li>
      <li class="active">[] Our Services</li>
      <li>[] Recent Productions</li>
      <li>[] Blog</li>
      <li>[] Testimonials</li>
      <li>[] Get a Quote</li>
      <li>[] Contact</li>
      <li>[] Film Library</li>
      <li>[] Showreel</li>
      <li>[] Film Location Guide</li>
      <li>[] Events</li>
    </ul>
  </nav>
  <ul class="abs submenu">
    <li>Our Services</li>
    <li>Crews</li>
    <li>Corporate Shoots</li>
    <li>Webcasts</li>
    <li>Production Arm</li>
    <li>Legal Videography</li>
  </ul>
  <div class="abs flag" aria-label="German language"></div>
  <div class="abs event-date">03.11.2010</div>
  <p class="abs event-text">Crew meet-up at the Frankfurt studio, with drinks and a look at new kit.</p>
  <a class="abs event-link" href="#">SEE ALL EVENTS</a>
  <div class="abs share">
    <span class="share-label">share</span>
    <span class="share-item"><i></i>Pals</span>
    <span class="share-item">Chirper</span>
    <span class="share-item">Tubecast</span>
  </div>
</header>

<div class="abs band"></div>
<div class="abs tab-row"></div>
<div class="abs tab tab-testimonials">testimonials</div>
<div class="abs tab tab-quote">get a quote</div>

<section class="abs feature"></section>
<blockquote class="abs quote">"We've been working with Hallow Pictures for many years now and it's always so reassuring to have Ewan and his team involved. They're all more like an extension of our own production team than a 'supplier', and the offices are really cool!"</blockquote>
<div class="abs quote-author">Harriet Lowry, PTV, London</div>
<a class="abs quote-more" href="#">&gt; Read All...</a>
<div class="abs divider"></div>
<form class="abs form">
  <span class="field-label">NAME</span><span class="field"></span>
  <span class="field-label">EMAIL</span><span class="field"></span>
  <span class="field-label">CONTACT NUMBER</span><span class="field"></span>
  <span class="btn">SEND</span><span class="btn">CLEAR</span>
  <p class="form-note">* A copy of this message will be sent to the address you have specified</p>
</form>
<div class="abs message-label">MESSAGE</div>
<div class="abs message"></div>

<div class="abs tab tab-clients">our clients</div>
<section class="abs clients"></section>
<svg class="abs arrow" style="left:0" width="60" height="160" viewBox="0 0 60 160"><path d="M50 20 L10 80 L50 140" stroke="#c40a0a" stroke-width="22" fill="none"/></svg>
<svg class="abs arrow" style="left:1140px" width="60" height="160" viewBox="0 0 60 160"><path d="M10 20 L50 80 L10 140" stroke="#c40a0a" stroke-width="22" fill="none"/></svg>
<div class="abs client" style="left:90px;top:1228px;width:190px">VCN</div>
<div class="abs client" style="left:300px;top:1232px;width:150px;font-size:22px">Quadrant TV</div>
<div class="abs client" style="left:460px;top:1228px;width:110px">Arc</div>
<div class="abs client" style="left:570px;top:1232px;width:130px;font-size:24px">Nordbay</div>
<div class="abs client" style="left:700px;top:1232px;width:120px;font-size:24px">Beat TV</div>
<div class="abs client" style="left:830px;top:1234px;width:130px;font-size:22px">Terra Atlas</div>
<div class="abs client" style="left:965px;top:1220px;width:170px;font-size:22px;line-height:26px">Horizon Network</div>

<main>
  <h1 class="abs intro-title">english speaking camera crews throughout germany and europe</h1>
  <div class="abs intro">
    <p>We set up Lens Troupe Nordic to meet the demands of a growing number of TV-producers whose working language is English. This is our Passion! Why else would we keep doing it for over 30 years! As a producer, you're bound to have great ideas...but how do you make them a reality in a country where you can't speak the language? Partner with us! We are native English speakers so nothing gets lost in translation. We'll catch hold of your vision, and with local know-how, we'll make it happen.</p>
    <p>No job is too big, too small, too hard, too far away, or too urgent. Try us!</p>
    <ul>
      <li>We provide camera crews and facilities throughout Germany and Europe</li>
      <li>We shoot in both PAL and NTSC</li>
      <li>We edit either in-studio or on the move and we transfer urgent footage via FTP or SNG</li>
      <li>We are on call 24/7</li>
    </ul>
    <p>To make a no obligation enquiry about any of our services, please call Frankfurt Headquarters: +49-69-000412 (Toll free from the USA 1-800-555-0147) or click here to <span class="link">get a quote</span></p>
  </div>

  <h2 class="abs reel-title">Our Showreel</h2>
  <div class="abs video" role="img" aria-label="Showreel video player"></div>
  <div class="abs video-name">lenstroupenordic</div>
  <svg class="abs play" width="40" height="40" viewBox="0 0 40 40"><circle cx="20" cy="20" r="19" fill="#333"/><path d="M15 11 L29 20 L15 29Z" fill="#fff"/></svg>
  <div class="abs controls"></div>
  <div class="abs social"><span>Like · 4</span><span>Follow us on Chirper</span></div>
  <h3 class="abs more">more to see...</h3>

  <div class="abs" style="left:600px;top:1838px">
    <div class="thumb" role="img" aria-label="Video still: shoot in Munich">lenstroupenordic</div>
    <p class="thumb-caption">&gt; Q4 shoot in Munich, Germany and Eindhoven, Netherlands</p>
  </div>
  <div class="abs" style="left:896px;top:1838px">
    <div class="thumb" role="img" aria-label="Video still: shoot in Brussels">lenstroupenordic</div>
    <p class="thumb-caption">&gt; RX7 shoot in Brussels with Promptline</p>
  </div>
  <div class="abs" style="left:600px;top:2056px">
    <div class="thumb" role="img" aria-label="Video still: shoot in Stuttgart">lenstroupenordic</div>
    <p class="thumb-caption">&gt; Q4 HD Vellmar shoot in Stuttgart, Germany</p>
  </div>
  <div class="abs" style="left:896px;top:2056px">
    <div class="thumb" role="img" aria-label="Video still: shoot in Schwanau">lenstroupenordic</div>
    <p class="thumb-caption">&gt; Kestrel 7K shoot in Schwanau, Germany</p>
  </div>
  <a class="abs see-all" href="#">&gt; See All...</a>
</main>

<footer class="abs footer">
  <div class="footer-nav">About Us &nbsp;|&nbsp; Our Services &nbsp;|&nbsp; Recent Productions &nbsp;|&nbsp; Blog &nbsp;|&nbsp; Testimonials &nbsp;|&nbsp; Get a Quote &nbsp;|&nbsp; Contact &nbsp;|&nbsp; Film Library &nbsp;|&nbsp; Showreel &nbsp;|&nbsp; Film Location Guide</div>
  <div class="footer-legal">Copyright 2010 - Privacy Policy &nbsp;|&nbsp; Terms &amp; Conditions</div>
</footer>

</body>
</html>
```